Ovaro Letterhead

Need a fresh looking design. We are a IT service company and I would like some elements of the logo to flow through. I have included the logo as an attachment. I have also included business card design as it might help with the design.

Industry/Entity Type

Business

```html
<!DOCTYPE html>
<html lang="en">
<head>
<meta charset="utf-8">
<title>Ovaro Letterhead</title>
<link rel="stylesheet" href="https://fonts.googleapis.com/css2?family=Varela+Round&display=swap">
<style>
  :root {
    --paper: #ffffff;
    --brand-green: #9acb3b;
    --brand-grey: #7b8084;
    --tint-green: #cfe6a2;
    --tint-grey: #c3c6c9;
  }
  html, body {
    margin: 0;
    padding: 0;
    overflow: hidden;
    background: var(--paper);
  }
  .letterhead {
    position: relative;
    width: 927px;
    height: 1200px;
    background: var(--paper);
    overflow: hidden;
  }
  .brand-name {
    position: absolute;
    left: 82px;
    top: 116px;
    margin: 0;
    font-family: "Varela Round", sans-serif;
    font-weight: 400;
    font-size: 64px;
    line-height: 1;
    letter-spacing: 1px;
    color: var(--brand-green);
  }
  .header-flow {
    position: absolute;
    left: 0;
    top: 0;
    width: 927px;
    height: 270px;
  }
</style>
</head>
<body>
  <main class="letterhead">
    <svg class="header-flow" viewBox="0 0 927 270" role="img"
         aria-label="Decorative stream of small green and grey squares flowing from the company name to the top right corner">
      <defs>
        <linearGradient id="flowTone" x1="0" y1="1" x2="1" y2="0">
          <stop offset="0" stop-color="var(--tint-grey)" stop-opacity="0.15"/>
          <stop offset="0.45" stop-color="var(--tint-green)" stop-opacity="0.5"/>
          <stop offset="1" stop-color="var(--tint-grey)" stop-opacity="0.75"/>
        </linearGradient>
      </defs>
      <path fill="url(#flowTone)"
            d="M250 118 C340 90 430 50 500 22 C540 8 575 2 606 0 L927 0 L927 258
               C870 235 810 212 758 197 C680 172 600 158 530 150 C430 136 330 124 250 121 Z"/>
    </svg>
    <p class="brand-name">Ovaro</p>
  </main>
</body>
</html>
```